Kellbrook Tutoring Flyer Design

I need a flyer for a new company based in Samford Valley called 'Kellbrook Tutoring'. We specialise in Mathematics tutoring for students from grade 5 up to grade twelve. We currently have a logo that has purple as its major colour. The final design should convey professionalism, compassion and that education is about maximising peoples possibilities,
Updates

Just thought I would let you know that my slogan is "Maximise your possibilities" and my phone number is 0438260917

Thanks.

My current logo doesn't seem to want to upload

Target Market(s)

The two targets are parents of students in grades 5-12 and students in grades 5-12

Industry/Entity Type

Education

Logo Text

Kellbrook Tutoring

Logo styles of interest
Pictorial/Combination Logo
Abstract Logo
Lettermark Logo
Requirements
Must have
• My slogan is "Maximise your possibilities"
my phone number is 0438260917

```html
<!DOCTYPE html>
<html lang="en">
<head>
<meta charset="utf-8">
<title>Kellbrook Tutoring — Maximise your possibilities</title>
<link href="https://fonts.googleapis.com/css2?family=Cinzel:wght@400;500&display=swap" rel="stylesheet">
<style>
  :root {
    --ink-dark: #1b1e1e;
    --umbrella-grey-deep: #202324;
    --umbrella-grey-mid: #3f4345;
    --umbrella-grey-light: #5c6062;
    --accent-yellow: #f1d71c;
    --accent-yellow-soft: rgba(241, 215, 28, 0.55);
    --gold-text: #f1c40a;
    --contact-purple: #2a0b8e;
  }
  html, body {
    margin: 0;
    padding: 0;
    width: 932px;
    height: 1200px;
    overflow: hidden;
    background: var(--ink-dark);
  }
  .flyer {
    position: relative;
    width: 932px;
    height: 1200px;
    overflow: hidden;
    background: var(--ink-dark);
    font-family: "Cinzel", "Trajan Pro", Georgia, serif;
    font-weight: 500;
    color: var(--gold-text);
  }
  .hero-photo {
    position: absolute;
    left: 0;
    top: 0;
    width: 932px;
    height: 689px;
    background:
      radial-gradient(circle 260px at 612px 378px,
        var(--accent-yellow) 0%,
        var(--accent-yellow) 45%,
        var(--accent-yellow-soft) 72%,
        rgba(241, 215, 28, 0) 100%),
      linear-gradient(180deg,
        var(--umbrella-grey-mid) 0%,
        var(--umbrella-grey-light) 40%,
        var(--umbrella-grey-mid) 75%,
        var(--umbrella-grey-deep) 100%);
  }
  .headline {
    position: absolute;
    left: 0;
    width: 100%;
    margin: 0;
    text-align: center;
    font-weight: 500;
    letter-spacing: 1px;
    line-height: 1;
    font-size: 72px;
  }
  .headline-top { top: 704px; }
  .headline-bottom { top: 786px; }
  .brand-name {
    position: absolute;
    left: 0;
    top: 869px;
    width: 100%;
    margin: 0;
    text-align: center;
    font-size: 34px;
    letter-spacing: 1px;
    line-height: 1;
  }
  .contact-bar {
    position: absolute;
    left: 0;
    top: 1147px;
    width: 932px;
    height: 53px;
    background: var(--contact-purple);
    display: flex;
    align-items: center;
    justify-content: center;
    font-size: 28px;
    letter-spacing: 1px;
  }
</style>
</head>
<body>
  <main class="flyer">
    <div class="hero-photo" role="img" aria-label="Photograph of a crowd of black umbrellas seen from above, with a single bright yellow umbrella standing out among them"></div>
    <h1 class="headline headline-top">Maximise</h1>
    <p class="headline headline-bottom">your possibilities</p>
    <p class="brand-name">Kellbrook Tutoring</p>
    <footer class="contact-bar">Contact&nbsp;0438260917</footer>
  </main>
</body>
</html>
```